Welcome Card Project for bow tie business

We need a welcome message card that will be placed inside a box (packaging) for a mens bow tie business 'Dorian Vellum'. Dorian Vellum is a men's brand specializing in unique bow ties of limited editions using quality designer fabrics.
Dorian Vellum is all about colour, prints and style, where the consumer can add a something a little out of the ordinary and quirky to break out of the mundane 9-5 day.

The dimensions of the double sided welcome card is as follows:
60mm H x 120mm W

One side of the welcome card will have the welcome message with colour and graphics in the background depicting happiness and excitement. It will also include the Chatterbook, quiller and Snapgrove logos and an invitation for customers to share pictures of them wearing the bow ties on Snapgrove and chatterbook. The website address will also be included here (www.dorianvellum.example)

The other side of the welcome card will be more conservative with a black on black paisley print design with the 'Dorian Vellum' logo in a deep purple colour.

Target Market(s)

Men, hipsters, fashionistas, working professionals, women seeking gifts for men

Industry/Entity Type

Conservative

Requirements
Must have
• - Double sided welcome card
- The welcome message (file attached) on one side of the card
- Chatterbook + Snapgrove logo
- Dorian Vellum website address (www.dorianvellum.example)
- Corporate colours: purple, black, orange (on website and in logo) + neutral recycled brown (packaging colour)
- Black on black paisley print on one side of the card
- Dorian Vellum logo (file attached)- colour: deep purple
Nice to have

Should not have
• - pictures of rainbows

```html
<!DOCTYPE html>
<html lang="en">
<head>
<meta charset="utf-8">
<title>Dorian Vellum – Welcome Card</title>
<link rel="stylesheet" href="https://fonts.googleapis.com/css2?family=Open+Sans:wght@400;600&display=swap">
<style>
  :root {
    --stage: #e8e5e1;
    --card-black: #0f1010;
    --card-black-sheen: #2c2e2d;
    --card-white: #f4f4f4;
    --purple-deep: #4f2160;
    --purple-mid: #7a3c8c;
    --purple-soft: #b48cc6;
    --ink: #2a2a2a;
    --white: #ffffff;
  }
  * { box-sizing: border-box; margin: 0; padding: 0; }
  html, body { width: 1200px; height: 900px; overflow: hidden; }
  body {
    background: var(--stage);
    font-family: "Open Sans", Arial, sans-serif;
    position: relative;
  }
  .card {
    position: absolute;
    left: 220px;
    width: 760px;
    height: 380px;
    overflow: hidden;
    box-shadow: 0 6px 18px rgba(0,0,0,.18);
  }

  /* Conservative side */
  .card--front {
    top: 40px;
    background: linear-gradient(115deg, var(--card-black) 0%, var(--card-black-sheen) 48%, var(--card-black) 72%);
  }
  .paisley-field {
    position: absolute;
    inset: 0;
    background:
      radial-gradient(ellipse 200px 150px at 50% 50%, rgba(150,152,150,.28) 0%, rgba(90,92,91,.14) 60%, rgba(0,0,0,0) 100%),
      radial-gradient(circle at 30% 30%, rgba(60,62,61,.35) 0%, rgba(0,0,0,0) 40%),
      radial-gradient(circle at 72% 70%, rgba(60,62,61,.35) 0%, rgba(0,0,0,0) 40%);
  }
  .brand-name {
    position: absolute;
    left: 0; right: 0; top: 150px;
    text-align: center;
    font-weight: 400;
    font-size: 56px;
    color: var(--purple-soft);
    letter-spacing: 1px;
  }

  /* Welcome message side */
  .card--back {
    top: 480px;
    background: var(--card-white);
  }
  .gift-ornament {
    position: absolute;
    left: 70px; top: 50px;
    width: 240px; height: 260px;
    border-radius: 45% 45% 20% 30%;
    background: radial-gradient(circle at 45% 40%, var(--purple-soft) 0%, var(--purple-mid) 50%, rgba(122,60,140,0) 78%);
  }
  .welcome-message {
    position: absolute;
    left: 250px; top: 28px;
    font-weight: 600;
    font-size: 14px;
    line-height: 17px;
    color: var(--ink);
    transform: rotate(8deg);
    transform-origin: left top;
    list-style: none;
    white-space: nowrap;
  }
  .welcome-message li:nth-child(2)  { padding-left: 30px; }
  .welcome-message li:nth-child(3)  { padding-left: 55px; }
  .welcome-message li:nth-child(4)  { padding-left: 150px; }
  .welcome-message li:nth-child(5)  { padding-left: 165px; padding-top: 8px; }
  .welcome-message li:nth-child(6)  { padding-left: 190px; }
  .welcome-message li:nth-child(7)  { padding-left: 255px; }
  .welcome-message li:nth-child(8)  { padding-left: 280px; }
  .welcome-message li:nth-child(9)  { padding-left: 300px; }
  .welcome-message li:nth-child(10) { padding-left: 345px; }
  .signature {
    position: absolute;
    right: 60px; top: 296px;
    font-size: 19px;
    font-weight: 400;
    color: var(--purple-deep);
  }
  .website {
    position: absolute;
    left: 22px; bottom: 30px;
    font-size: 13px;
    font-weight: 600;
    color: var(--purple-deep);
  }
  .social-tab {
    position: absolute;
    left: 240px; right: 0; bottom: 26px;
    height: 24px;
    background: var(--purple-deep);
    color: var(--white);
    font-size: 10px;
    display: flex;
    align-items: center;
    justify-content: flex-end;
    gap: 14px;
    padding: 0 20px;
    white-space: nowrap;
  }
  .social { display: flex; align-items: center; gap: 5px; }
  .social-mark {
    width: 12px; height: 12px;
    background: var(--white);
    display: inline-block;
  }
  .share-band {
    position: absolute;
    left: 0; right: 0; bottom: 0;
    height: 26px;
    background: var(--purple-deep);
    color: var(--white);
    font-size: 11px;
    display: flex;
    align-items: center;
    padding: 0 22px;
    white-space: nowrap;
  }
</style>
</head>
<body>
  <section class="card card--front" aria-label="Card front">
    <div class="paisley-field" role="img" aria-label="Black-on-black swirling paisley ornament"></div>
    <h1 class="brand-name">Dorian Vellum</h1>
  </section>

  <section class="card card--back" aria-label="Card back with welcome message">
    <div class="gift-ornament" role="img" aria-label="Purple swirls and flowers bursting from an open gift box"></div>
    <ul class="welcome-message">
      <li>This is only the beginning.</li>
      <li>Your Dorian Vellum bow tie</li>
      <li>is an adventure for you to unfold.</li>
      <li>unexpected and new.</li>
      <li>Wear it on a night out,</li>
      <li>or bring a dash of colour to work,</li>
      <li>dream with it,</li>
      <li>wear it on a rainy day,</li>
      <li>create new memories</li>
      <li>and be surprised.</li>
    </ul>
    <p class="signature">Dorian Vellum</p>
    <p class="website">www.dorianvellum.example</p>
    <div class="social-tab">
      <span class="social"><i class="social-mark"></i>Chatterbook /dorianvellum</span>
      <span class="social"><i class="social-mark"></i>quiller @dorianvellum</span>
      <span class="social"><i class="social-mark"></i>Snapgrove /dorianvellum</span>
    </div>
    <div class="share-band">Share your picture with Dorian Vellum bow tie here.... and share the fun!</div>
  </section>
</body>
</html>
```